Bottled Margarita Label Project

We need a label design (using a 750 ml bottle) for an all natural, premium, Ready to Drink (as in pre-mixed) Margarita. The brand is called VONDRA Pure Margarita. We were tired of the chemical, sugary, preservative laden "margaritas" with artificial colorings and cheap tequilas, so we developed a simple, straightforward CLASSIC, ingredient driven margarita made with only the purest, traditional ingredients: 100% Blue Agave Tequila Reposado, Double Distilled Orange Liqueur, Lime Juice and sweetened with Organic Cane Sugar. The result is a pure margarita, the kind you got on that amazing beach vacation in Mexico. This is a product that can be chilled and served over ice or straight up. You might grab one to take to a BBQ or to the beach. It's simple, sexy and classic. We are hoping the final design can communicate purity, integrity of ingredients and the freedom one might feel when on vacation in the sun. This doesnt have to be a Latin themed beverage, but more of a Summer / chill / "sala del oro" in a bottle vibe. Thank you!

Target Market(s)

25 to 45 year olds who feel they know what makes up a good margarita. Aspirational types who love adventurous vacations but are not necessarily wealthy. Our customer doesn't always have the time to make a real margarita from scratch but wish they could get a decent one in a bottle that doesn't taste artificial. They are brand and label conscious and will pay a little more for quality as long as there is value.

Industry/Entity Type

Cafe

Requirements
Must have
• Must have "Vondra" and "pure margartia" clearly listed as the name of the beverage. Must also make clear that this is "Premium", "Ready to Drink" and "Made with 100% Blue Agave Tequila"
Nice to have
• We really love designs that are clean and uncluttered. We have imagined a clear 750ml bottle. Think about tequila when you think about this label. This is a hand made, artisan product produced in batches. We are looking for a finished label/bottle that is colorful, transcendent, artisinal and timeless. It should be mature but not stuffy. It should be simple and sexy - not splashy, brash or silly. Our competition is Tidy Moth Margarita, Rafa Tolentes, and Brevo pre-mixed margaritas which are fake margaritas made in huge factories. Vondra is made with integrity and honest ingredients. For colors, greens come to mind but we are totally open to a designer's vision ;). This should be a product that a fashion forward airline like Halcyon Skyways would want serve and a bottle that a savvy drinker would choose over the bland, mainstream brands. Check out Munrez Cachaça for a sexy, vibrant take on a bottle of alcohol with a Summer slant. Also look at Velquiro tequila. They have a wonderful label that blends vintage and modern elements with minimalist design and comes off as handmade.
Should not have
• Elements we do NOTwant to see any red colors, sombreros, parrots, tiki masks, palm trees, spring break, deserted islands, or Dale Hornsby imagery. This should be a product that an airline like Halcyon Skyways would want to serve.

```html
<!DOCTYPE html>
<html lang="en">
<head>
<meta charset="utf-8">
<title>VONDRA Pure Margarita – Label</title>
<link rel="stylesheet" href="https://fonts.googleapis.com/css2?family=Alegreya:wght@400;500&family=Spectral:wght@500&display=swap">
<style>
  :root {
    --page: #eef1f0;
    --label-top: #cfd9d3;
    --label-mid: #a9d3cf;
    --label-low: #63bfc3;
    --label-edge: #4fb3bd;
    --brand-teal: #1d9a86;
    --ink: #3b3e40;
    --rule: #5a5f60;
    --lime: #8fbf3a;
    --lime-pith: #d6e6a0;
  }
  html, body {
    margin: 0;
    width: 1200px;
    height: 1169px;
    overflow: hidden;
    background: var(--page);
  }
  .label {
    position: absolute;
    left: 273px;
    top: 55px;
    width: 654px;
    height: 1060px;
    overflow: hidden;
    background:
      linear-gradient(90deg, rgba(255,255,255,0) 55%, rgba(60,170,185,0.35) 100%),
      linear-gradient(180deg, var(--label-top) 0%, var(--label-mid) 45%, var(--label-low) 80%, var(--label-edge) 100%);
    font-family: "Alegreya", serif;
    color: var(--ink);
  }
  .claims {
    position: absolute;
    left: 14px;
    top: 60px;
    margin: 0;
    padding: 0;
    list-style: none;
    font-size: 22px;
    line-height: 36px;
    font-style: italic;
  }
  .claims li {
    display: flex;
    align-items: baseline;
    gap: 6px;
  }
  .claims li::before {
    content: "";
    display: inline-block;
    width: 14px;
    border-bottom: 1.5px solid var(--rule);
  }
  .claims .trail {
    display: inline-block;
    border-bottom: 1.5px solid var(--rule);
  }
  .product-name {
    position: absolute;
    left: 180px;
    top: 520px;
    margin: 0;
    font-weight: 400;
    font-size: 72px;
    line-height: 68px;
    color: var(--ink);
  }
  .brand {
    position: absolute;
    left: 455px;
    top: 40px;
    width: 175px;
    height: 960px;
    margin: 0;
    writing-mode: vertical-rl;
    transform: rotate(180deg);
    text-align: start;
    font-family: "Spectral", serif;
    font-weight: 500;
    font-size: 178px;
    line-height: 175px;
    letter-spacing: 4px;
    color: var(--brand-teal);
  }
  .lime {
    position: absolute;
    left: -110px;
    top: 890px;
    width: 330px;
    height: 330px;
    border-radius: 50%;
    background: radial-gradient(circle, var(--lime-pith) 0%, var(--lime) 55%, #5f9a25 100%);
  }
  .volume {
    position: absolute;
    left: 258px;
    top: 980px;
    margin: 0;
    font-size: 23px;
    color: var(--ink);
  }
</style>
</head>
<body>
  <main class="label">
    <ul class="claims">
      <li>ready to drink <span class="trail" style="width:120px"></span></li>
      <li>premium ingredients <span class="trail" style="width:80px"></span></li>
      <li>made with 100% blue agave tequila</li>
    </ul>
    <h2 class="product-name">pure<br>margarita</h2>
    <h1 class="brand">VONDRA</h1>
    <div class="lime" role="img" aria-label="Slice of fresh lime"></div>
    <p class="volume">45% alc. 750 ml</p>
  </main>
</body>
</html>
```